Banner and logo redesign for B2B website

I want a new email banner design and logo. This is for a B2B whitepaper library hosting content and resources of technology companies.https://qz.brimvalen.com/

Target Market(s)

B2B

Industry/Entity Type

tech B2B

Number of Pages Required

1 page

Font styles to use
Sans Serif

Requirements
Must have
• A logo and email banner
Nice to have
• Similar colour pallet to what can be found on the site
Should not have
• website designs

```html
<!DOCTYPE html>
<html lang="en">
<head>
<meta charset="utf-8">
<title>Brimvalen – Monthly Newsletter Banner</title>
<link rel="stylesheet" href="https://fonts.googleapis.com/css2?family=Outfit:wght@400;500;700;800&display=swap">
<style>
  :root {
    --navy-deep: #0b1440;
    --navy: #13205a;
    --navy-arc: #0e1a4e;
    --violet: #5a4cf2;
    --violet-soft: #6f5ff7;
    --cyan: #3fd0e6;
    --pink: #e05aa8;
    --white: #ffffff;
    --muted: #dfe4ff;
  }
  * { box-sizing: border-box; margin: 0; padding: 0; }
  html, body { width: 1200px; height: 646px; overflow: hidden; background: var(--navy-deep); }
  .banner {
    position: relative;
    width: 1200px;
    height: 646px;
    overflow: hidden;
    background: linear-gradient(120deg, var(--navy-deep) 0%, var(--navy) 55%, #1b2a78 100%);
    font-family: "Outfit", sans-serif;
    color: var(--white);
  }
  .banner__shapes { position: absolute; inset: 0; }
  .brand {
    position: absolute;
    left: 64px;
    top: 44px;
    display: flex;
    align-items: center;
    gap: 12px;
  }
  .brand__dot {
    width: 38px;
    height: 38px;
    border-radius: 50%;
    background: var(--white);
  }
  .brand__name {
    font-weight: 700;
    font-size: 26px;
    letter-spacing: 0.5px;
    color: var(--white);
  }
  .tagline {
    position: absolute;
    left: 66px;
    top: 124px;
    font-weight: 500;
    font-size: 21px;
    color: var(--muted);
  }
  .headline {
    position: absolute;
    left: 64px;
    top: 166px;
    font-weight: 800;
    font-size: 74px;
    line-height: 84px;
    text-transform: uppercase;
    letter-spacing: 0.5px;
  }
  .headline__light { font-weight: 400; }
  .site-url {
    position: absolute;
    left: 66px;
    top: 580px;
    font-weight: 700;
    font-size: 22px;
  }
  .hero-photo {
    position: absolute;
    left: 720px;
    top: 50px;
    width: 440px;
    height: 596px;
    border-radius: 220px 220px 0 0;
    background: linear-gradient(180deg, #3a3450 0%, #4a6b8c 45%, #2f4d6e 100%);
  }
</style>
</head>
<body>
  <main class="banner">
    <svg class="banner__shapes" width="1200" height="646" viewBox="0 0 1200 646" aria-hidden="true">
      <circle cx="250" cy="230" r="520" fill="var(--navy-arc)" opacity="0.7"/>
      <path d="M 820 -40 A 520 520 0 0 1 1010 646" fill="none" stroke="var(--cyan)" stroke-width="2" opacity="0.8"/>
      <path d="M 1130 -20 A 400 400 0 0 1 1200 120" fill="none" stroke="var(--pink)" stroke-width="3"/>
      <circle cx="1000" cy="370" r="330" fill="var(--violet)"/>
      <circle cx="1000" cy="370" r="330" fill="none" stroke="var(--violet-soft)" stroke-width="2"/>
    </svg>

    <div class="brand">
      <span class="brand__dot"></span>
      <span class="brand__name">BRIMVALEN</span>
    </div>

    <p class="tagline">Get your curated monthly newsletter</p>

    <h1 class="headline">
      Stay ahead<br>
      with <span class="headline__light">the latest in</span><br>
      Brimvalen
    </h1>

    <p class="site-url">www.brimvalen.com</p>

    <div class="hero-photo" role="img" aria-label="Photo of a smiling young man in glasses and a blue t-shirt typing on a laptop"></div>
  </main>
</body>
</html>
```